Motor Vault Website - Part of the Brantley Group

A complimentary website is required for the launch of a 'Motor Vault' - a new service launched by industry renowned BRANTLEY. Motor Vault is an industry-first brand that designs and builds unique subterranean car parks for private residential homes in London and the influential counties within the UK. Please see here the direction of a new BRANTLEY Website - we would like Motor Vault to be complimentary and sit alongside BRANTLEY harmoniously - https://www.brantleyhq.example/brantley-nu-staging Brantley have some images, but whilst more professional images are in production - we have also attached pixmoor photos- named clearly as pixmoor. **Attached files include JPEG, .eps of logo and Brantley library images and Pixmoor Library Images - two versions of logo dependent on background colour. - Website needs to be sleek, chic and masculine.- Colour Palette - Grey/ Black/ White - Same visiual journey as Brantley website- Required areas within the sit include - About Us / Our Work / Contact Page

Target Market(s)

Luxury
Men

Number of Pages Required

2 page

Font styles to use
Sans Serif

Colors
e8e8e8
757575
1b1b1b
000000
9d9d9d
cbcbcb
f5f5f5

Requirements
Must have
• Complimentary of this site - https://www.brantleyhq.example/brantley-nu-staging
Should not have
• Colour

```html
<!DOCTYPE html>
<html lang="en">
<head>
<meta charset="utf-8">
<title>Motor Vault</title>
<link rel="stylesheet" href="https://fonts.googleapis.com/css2?family=Raleway:wght@400;500;600;700;800&display=swap">
<style>
:root{
  --bar:#e8e8e8;
  --ink:#000000;
  --deep:#1b1b1b;
  --mid:#757575;
  --soft:#9d9d9d;
  --light:#cbcbcb;
  --paper:#ffffff;
}
*{margin:0;padding:0;box-sizing:border-box}
html,body{width:1200px;height:2507px;overflow:hidden}
body{position:relative;background:var(--paper);color:var(--ink);font-family:'Raleway',sans-serif}
.abs{position:absolute}

.site-header{left:0;top:0;width:1200px;height:62px;background:var(--bar)}
.brand{left:234px;top:12px}
.brand-name{font-weight:700;font-size:28px;letter-spacing:.5px;line-height:28px;display:flex;align-items:center;gap:8px}
.brand-name .mark{width:18px;height:18px;background:currentColor;display:inline-block}
.brand-tag{font-size:6px;letter-spacing:1px;text-transform:uppercase;color:var(--mid);margin-left:46px;margin-top:2px}
.main-nav{left:546px;top:22px;display:flex;gap:16px;font-weight:700;font-size:15px}
.social-mini{left:914px;top:23px;display:flex;gap:5px}
.social-mini span{width:13px;height:13px;background:var(--deep);display:block}

.hero{left:0;top:62px;width:1200px;height:563px;background:radial-gradient(ellipse at 50% 55%,#6a6a6a 0%,#3a3a3a 35%,#1b1b1b 70%,#0a0a0a 100%)}
.hero-title{left:0;top:278px;width:1200px;text-align:center;color:#fff;font-weight:800;font-size:29px;line-height:36px}
.btn-outline{left:511px;top:368px;width:187px;height:32px;border:2px solid #fff;border-radius:5px;color:#fff;font-weight:700;font-size:17px;display:flex;align-items:center;justify-content:center}

.section-title{left:0;width:1200px;text-align:center;font-weight:600;font-size:38px}
.copy{font-size:18.5px;line-height:22.5px}
.btn-solid{background:var(--ink);color:#fff;border-radius:4px;font-weight:700;display:flex;align-items:center;justify-content:center}

.photo{background:linear-gradient(135deg,#d6d6d6,#5a5a5a 60%,#1b1b1b)}
.work-grid{left:234px;top:1385px;width:732px;display:grid;grid-template-columns:repeat(3,237px);grid-template-rows:156px 156px;column-gap:10px;row-gap:6px}
.work-grid div:nth-child(odd){background:linear-gradient(160deg,#2a2a2a,#8a8a8a 50%,#1b1b1b)}
.work-grid div:nth-child(even){background:linear-gradient(200deg,#9d9d9d,#3a3a3a 55%,#111)}

.field{left:632px;width:334px;height:30px;border:2px solid var(--ink);border-radius:5px;display:flex;align-items:center;overflow:hidden;font-size:18px}
.field .icon{width:58px;height:100%;background:var(--ink);display:flex;align-items:center;justify-content:center}
.field .label{padding-left:10px}
.message{left:632px;top:2065px;width:334px;height:129px;border:2px solid var(--ink);border-radius:6px;padding:6px 12px;font-size:18px}

.site-footer{left:0;top:2381px;width:1200px;height:126px;background:var(--ink);color:#fff}
.foot-col{top:22px}
.foot-col h4{font-size:14px;font-weight:700;margin-bottom:8px}
.foot-col li{list-style:none;font-size:10.5px;line-height:13px;display:flex;align-items:center;gap:6px}
.foot-social{display:flex;gap:8px;margin-top:12px}
.foot-social span{width:20px;height:20px;background:#fff;display:block}
.copyright{left:0;top:2492px;width:1200px;text-align:center;font-size:7px;color:#fff}
</style>
</head>
<body>

<header class="site-header abs">
  <div class="brand abs">
    <div class="brand-name"><span class="mark"></span>MOTOR VAULT</div>
    <div class="brand-tag">Part of the Brantley Group</div>
  </div>
  <nav class="main-nav abs"><span>HOME</span><span>ABOUT US</span><span>OUR WORK</span><span>CONTACT US</span></nav>
  <div class="social-mini abs"><span></span><span></span><span></span></div>
</header>

<section class="hero abs" role="img" aria-label="Dim concrete underground car park with rows of columns"></section>
<h1 class="hero-title abs">First Brand That Designs &amp; Builds Unique<br>Subterranean Car Parks</h1>
<div class="btn-outline abs">DISCOVER NOW</div>

<h2 class="section-title abs" style="top:740px">About Us</h2>
<p class="copy abs" style="left:234px;top:804px;width:732px">Lorem Ipsum is simply dummy text of the printing and typesetting industry. Lorem Ipsum has been the industry's standard dummy text ever since the 1500s, anunprinter took a galley of type and scrambled it to make a type specimen book.</p>
<p class="copy abs" style="left:234px;top:873px;width:346px">Lorem Ipsum is simply dummy text of the printing and typesetting industry. Lorem Ipsum has been the industry's standard dummy text ever since the 1500s, when an unknown printer took a galley of type and scrambled it to make a type specimen book.</p>
<div class="photo abs" style="left:590px;top:879px;width:376px;height:209px" role="img" aria-label="Close-up of a silver alloy car wheel"></div>
<div class="btn-solid abs" style="left:234px;top:1058px;width:157px;height:30px;font-size:18px">LEARN MORE</div>

<h2 class="section-title abs" style="top:1203px">Our Work</h2>
<p class="copy abs" style="left:234px;top:1267px;width:732px">Lorem Ipsum is simply dummy text of the printing and typesetting industry. Lorem Ipsum has been the industry's standard dummy text ever since the 1500s, when an unknown printer took a galley of type and scrambled it to make a type specimen book.</p>
<div class="work-grid abs">
  <div role="img" aria-label="Welding sparks on a steel structure"></div>
  <div role="img" aria-label="Steel framework seen from below"></div>
  <div role="img" aria-label="Finished underground bay with lighting"></div>
  <div role="img" aria-label="Light beam in an excavated basement"></div>
  <div role="img" aria-label="Digger working under a building"></div>
  <div role="img" aria-label="Excavation site beneath a structure"></div>
</div>
<div class="btn-solid abs" style="left:538px;top:1736px;width:124px;height:29px;font-size:14px">SEE MORE</div>

<h2 class="section-title abs" style="top:1880px">Contact Us</h2>
<p class="copy abs" style="left:234px;top:1944px;width:380px">Lorem Ipsum is simply dummy text of the printing and typesetting industry. Lorem Ipsum has been the industry's standard dummy text ever since the 1500s, when an unknown printer took a galley of type and scrambled it to make a type specimen book. It has survived not only five centuries, but also the leap into electronic typesetting, remaining essentially unchanged.</p>
<div class="field abs" style="top:1950px">
  <span class="icon"><svg width="14" height="16" viewBox="0 0 14 16"><circle cx="7" cy="4.5" r="3.5" fill="#fff"/><path d="M1 15c0-4 3-6 6-6s6 2 6 6z" fill="#fff"/></svg></span>
  <span class="label">Name</span>
</div>
<div class="field abs" style="top:2010px">
  <span class="icon"><svg width="16" height="12" viewBox="0 0 16 12"><rect x="0.5" y="0.5" width="15" height="11" fill="#fff"/><path d="M1 1l7 6 7-6" fill="none" stroke="#000" stroke-width="1.3"/></svg></span>
  <span class="label">Email</span>
</div>
<div class="message abs">Your Text Here</div>
<div class="btn-solid abs" style="left:632px;top:2226px;width:155px;height:30px;font-size:18px">SUBMIT</div>

<footer class="site-footer abs">
  <div class="brand-name abs" style="left:234px;top:48px;font-size:28px"><span class="mark"></span>MOTOR VAULT</div>
  <div class="brand-tag abs" style="left:234px;top:80px;margin:0 0 0 46px;color:var(--soft)">Part of the Brantley Group</div>
  <div class="foot-col abs" style="left:530px">
    <h4>Contact Us</h4>
    <ul>
      <li><svg width="8" height="10" viewBox="0 0 8 10"><path d="M4 10L1 5a3 3 0 1 1 6 0z" fill="#fff"/><circle cx="4" cy="4" r="1.2" fill="#000"/></svg>48 Harrow Yard Rd</li>
      <li><svg width="8" height="10" viewBox="0 0 8 10"><path d="M1 1h2l1 2-1 1c.5 1.5 1.5 2.5 3 3l1-1 1 2v2C4 10 0 6 1 1z" fill="#fff"/></svg>555-014-2290</li>
      <li><svg width="9" height="7" viewBox="0 0 9 7"><rect width="9" height="7" fill="#fff"/><path d="M0 0l4.5 4L9 0" fill="none" stroke="#000" stroke-width=".8"/></svg>hello@motorvault.example</li>
    </ul>
  </div>
  <div class="foot-col abs" style="left:724px;top:26px">
    <h4>Legal Info</h4>
    <ul><li>Terms Of Use</li><li>Privacy Policy</li><li>Copyright Policy</li></ul>
  </div>
  <div class="foot-col abs" style="left:881px;top:30px">
    <h4>Follow Us</h4>
    <div class="foot-social"><span></span><span></span><span></span></div>
  </div>
</footer>
<div class="copyright abs">copyright © 2018.</div>

</body>
</html>
```